Driftwater

Club flyer, grand opening night, house/electronic music, looking for clean design with a sample image attached. Please look at the prior flyers to get an idea of the style. Guaranteed project
I would like to use the red design if possible (driftwater flyer attached)
Text:
DRIFTWATER
Winter House Music Monthly
Opening Night Dec 13 2013
Tessaline (use logo)
Featuring
BRONTIK (House/Garage)
(use logo with just Brontik name)
w/ resident
ZEV (Pinwheel)
Free All Night
Target Market(s)
21-39 year old club with all house/electronic music. classier and grown up over gimmicky
Industry/Entity Type
Club
Look and feel

```html
<!DOCTYPE html>
<html lang="en">
<head>
<meta charset="utf-8">
<title>Driftwater – Winter House Music Monthly flyers</title>
<link href="https://fonts.googleapis.com/css2?family=Oswald:wght@300;500;700&family=Questrial&display=swap" rel="stylesheet">
<style>
  :root {
    --board-light: #a4a4a4;
    --board-dark: #1e1e1e;
    --footer-band: #6b6b6b;
    --ink: #0d0d0d;
    --paper-white: #ffffff;
    --rose-paper: #b26b7b;
    --rose-paper-deep: #8e4d62;
    --rose-photo-hot: #d8432c;
    --rose-photo-deep: #5a1f34;
    --rose-accent: #e2301f;
    --sand-paper: #cdb391;
    --sand-paper-deep: #a88a6c;
    --sand-photo-hot: #e5b332;
    --sand-photo-deep: #4a2a1c;
    --sand-accent: #f0a020;
  }
  * { margin: 0; padding: 0; box-sizing: border-box; }
  html, body { width: 1200px; height: 900px; overflow: hidden; }
  body {
    position: relative;
    background: linear-gradient(135deg, var(--board-light) 0%, #6a6a6a 45%, var(--board-dark) 100%);
    font-family: "Questrial", "Century Gothic", sans-serif;
  }
  .footer-band {
    position: absolute; left: 0; top: 790px; width: 1200px; height: 110px;
    background: var(--footer-band);
  }
  .flyer {
    position: absolute; top: 62px; width: 490px; height: 673px;
    box-shadow: 3px 4px 10px rgba(0,0,0,.55);
    display: block;
  }
  .flyer--rose { left: 67px; }
  .flyer--sand { left: 600px; }

  .headline { font-family: "Oswald", "Arial Narrow", sans-serif; font-weight: 700; fill: var(--paper-white); }
  .tagline { font-family: "Questrial", sans-serif; font-size: 18px; }
  .date-strong { font-family: "Oswald", sans-serif; font-weight: 500; fill: var(--ink); }
  .date-light { font-family: "Oswald", sans-serif; font-weight: 300; fill: var(--ink); }
  .act-name { font-family: "Oswald", sans-serif; font-weight: 700; font-size: 30px; fill: #f4f4f4; }
  .free-entry { font-family: "Questrial", sans-serif; font-size: 19px; fill: var(--paper-white); }
  .venue-name { font-family: "Questrial", sans-serif; font-size: 21px; letter-spacing: 1px; }
  .resident-name { font-family: "Questrial", sans-serif; font-size: 30px; }
  .web-address { font-family: "Questrial", sans-serif; font-size: 21px; }

  .flyer--rose .tagline { fill: var(--rose-accent); }
  .flyer--rose .accent-bar { fill: var(--rose-accent); }
  .flyer--rose .venue-name { fill: #7d3d52; opacity: .6; }
  .flyer--rose .resident-name { fill: #6a3a78; opacity: .6; }
  .flyer--rose .web-address { fill: #e6b9c6; opacity: .85; }

  .flyer--sand .tagline { fill: var(--sand-accent); }
  .flyer--sand .accent-bar { fill: #c96a1e; }
  .flyer--sand .venue-name { fill: #6f5040; opacity: .6; }
  .flyer--sand .resident-name { fill: #7a4d66; opacity: .55; }
  .flyer--sand .web-address { fill: #f2e6d4; opacity: .9; }
</style>
</head>
<body>

<svg class="flyer flyer--rose" viewBox="0 0 490 673" xmlns="http://www.w3.org/2000/svg">
  <defs>
    <linearGradient id="rose-paper" x1="0" y1="0" x2="1" y2="1">
      <stop offset="0" stop-color="var(--rose-paper-deep)"/>
      <stop offset=".5" stop-color="var(--rose-paper)"/>
      <stop offset="1" stop-color="var(--rose-paper-deep)"/>
    </linearGradient>
    <linearGradient id="rose-photo" x1="0" y1="0" x2="1" y2="1">
      <stop offset="0" stop-color="#8a2a4a"/>
      <stop offset=".35" stop-color="var(--rose-photo-hot)"/>
      <stop offset=".7" stop-color="var(--rose-photo-deep)"/>
      <stop offset="1" stop-color="#111"/>
    </linearGradient>
    <pattern id="rose-stripes" width="8" height="6" patternUnits="userSpaceOnUse">
      <rect width="8" height="6" fill="#9a8a8e" opacity=".3"/>
      <rect width="8" height="2" fill="#2a2a2a" opacity=".5"/>
    </pattern>
  </defs>
  <rect class="paper" width="490" height="673" fill="url(#rose-paper)"/>
  <polygon role="img" aria-label="Photo of the headline DJ in warm red club light" points="0,0 490,0 490,624 0,151" fill="url(#rose-photo)"/>
  <g class="diagonal" transform="translate(53,56) rotate(44)">
    <rect class="date-band" x="-200" y="5" width="1100" height="100" fill="url(#rose-stripes)"/>
    <rect x="40" y="-96" width="390" height="28" fill="var(--ink)"/>
    <text class="tagline" x="62" y="-76" textLength="340" lengthAdjust="spacingAndGlyphs">WINTER HOUSE MUSIC MONTHLY</text>
    <text class="headline" x="0" y="0" font-size="80" textLength="520" lengthAdjust="spacingAndGlyphs">DRIFTWATER</text>
    <text x="120" y="84" font-size="44" textLength="480" lengthAdjust="spacingAndGlyphs"><tspan class="date-strong">OPENING NIGHT </tspan><tspan class="date-light">DEC 13 2013</tspan></text>
  </g>
  <text class="act-name" x="303" y="62" textLength="155" lengthAdjust="spacingAndGlyphs">BRONTIK</text>
  <rect x="0" y="391" width="201" height="25" fill="var(--ink)"/>
  <text class="free-entry" x="27" y="411">FREE ALL NIGHT</text>
  <rect class="accent-bar" x="33" y="418" width="165" height="5"/>
  <text class="venue-name" x="168" y="545" text-anchor="middle">TESSALINE</text>
  <text class="resident-name" x="30" y="603" textLength="283" lengthAdjust="spacingAndGlyphs">ZEV · PINWHEEL</text>
  <text class="web-address" x="30" y="643" textLength="280" lengthAdjust="spacingAndGlyphs">WWW.driftwater.com</text>
</svg>

<svg class="flyer flyer--sand" viewBox="0 0 490 673" xmlns="http://www.w3.org/2000/svg">
  <defs>
    <linearGradient id="sand-paper" x1="0" y1="0" x2="1" y2="1">
      <stop offset="0" stop-color="var(--sand-paper-deep)"/>
      <stop offset=".5" stop-color="var(--sand-paper)"/>
      <stop offset="1" stop-color="var(--sand-paper-deep)"/>
    </linearGradient>
    <linearGradient id="sand-photo" x1="0" y1="0" x2="1" y2="1">
      <stop offset="0" stop-color="#b56a2a"/>
      <stop offset=".35" stop-color="var(--sand-photo-hot)"/>
      <stop offset=".7" stop-color="var(--sand-photo-deep)"/>
      <stop offset="1" stop-color="#111"/>
    </linearGradient>
    <pattern id="sand-stripes" width="8" height="6" patternUnits="userSpaceOnUse">
      <rect width="8" height="6" fill="#b0a898" opacity=".3"/>
      <rect width="8" height="2" fill="#2a2a2a" opacity=".5"/>
    </pattern>
  </defs>
  <rect class="paper" width="490" height="673" fill="url(#sand-paper)"/>
  <polygon role="img" aria-label="Photo of the headline DJ in warm amber club light" points="0,0 490,0 490,624 0,151" fill="url(#sand-photo)"/>
  <g class="diagonal" transform="translate(53,56) rotate(44)">
    <rect class="date-band" x="-200" y="5" width="1100" height="100" fill="url(#sand-stripes)"/>
    <rect x="40" y="-96" width="390" height="28" fill="var(--ink)"/>
    <text class="tagline" x="62" y="-76" textLength="340" lengthAdjust="spacingAndGlyphs">WINTER HOUSE MUSIC MONTHLY</text>
    <text class="headline" x="0" y="0" font-size="80" textLength="520" lengthAdjust="spacingAndGlyphs">DRIFTWATER</text>
    <text x="120" y="84" font-size="44" textLength="480" lengthAdjust="spacingAndGlyphs"><tspan class="date-strong">OPENING NIGHT </tspan><tspan class="date-light">DEC 13 2013</tspan></text>
  </g>
  <text class="act-name" x="303" y="62" textLength="155" lengthAdjust="spacingAndGlyphs">BRONTIK</text>
  <rect x="0" y="391" width="201" height="25" fill="var(--ink)"/>
  <text class="free-entry" x="27" y="411">FREE ALL NIGHT</text>
  <rect class="accent-bar" x="33" y="418" width="165" height="5"/>
  <text class="venue-name" x="168" y="545" text-anchor="middle">TESSALINE</text>
  <text class="resident-name" x="30" y="603" textLength="283" lengthAdjust="spacingAndGlyphs">ZEV · PINWHEEL</text>
  <text class="web-address" x="30" y="643" textLength="280" lengthAdjust="spacingAndGlyphs">WWW.driftwater.com</text>
</svg>

<div class="footer-band"></div>
</body>
</html>
```